Willowmere Chiropractic 20th Birthday Party

We are a holistic health practice focussing on women's children's health and we need a poster and an invitation to our 20th birthday celebration.

On Sat Nov 24th 12-3pm at WCC

```html
<!DOCTYPE html>
<html lang="en">
<head>
<meta charset="utf-8">
<title>Willowmere Chiropractic 20th Birthday Celebration</title>
<link href="https://fonts.googleapis.com/css2?family=Oswald:wght@700&family=Arimo:wght@400;700&display=swap" rel="stylesheet">
<style>
  :root {
    --teal: #4fc3bf;
    --navy: #1f5f8b;
    --red: #b52a1a;
    --border-blue: #2f3f9e;
    --white: #ffffff;
    --backdrop: #e9ecef;
    --party-top: #6fb3e8;
    --party-mid: #d9679a;
    --party-low: #e9b94a;
    --party-bottom: #5aa7d6;
  }
  * { margin: 0; padding: 0; box-sizing: border-box; }
  html, body { width: 1200px; height: 1200px; overflow: hidden; background: var(--backdrop); }
  .poster {
    position: absolute; left: 204px; top: 40px; width: 791px; height: 1119px; overflow: hidden;
  }
  .balloon-backdrop {
    position: absolute; inset: 0;
    background: linear-gradient(180deg, var(--party-top) 0%, var(--party-mid) 45%, var(--party-low) 75%, var(--party-bottom) 100%);
  }
  .logo-block {
    position: absolute; left: 255px; top: 0; width: 281px; height: 251px;
    background: var(--teal);
    display: flex; flex-direction: column; align-items: center; justify-content: center; gap: 18px;
  }
  .logo-dot { width: 46px; height: 46px; border-radius: 50%; background: var(--white); }
  .logo-name {
    font-family: "Arimo", sans-serif; font-weight: 700; font-size: 27px; line-height: 1.15;
    color: var(--white); text-align: center;
  }
  .invite-card {
    position: absolute; left: 71px; top: 270px; width: 649px; height: 795px;
    background: var(--white);
  }
  .invite-frame {
    position: absolute; inset: 16px 15px 14px 15px; border: 4px solid var(--border-blue);
  }
  .line {
    position: absolute; left: 0; width: 100%; text-align: center; white-space: nowrap;
  }
  .headline { font-family: "Oswald", sans-serif; font-weight: 700; font-size: 72px; line-height: 1; transform: scaleX(1.1); }
  .headline-years { top: 88px; color: var(--navy); }
  .headline-birthday { top: 182px; color: var(--red); }
  .headline-celebration { top: 277px; color: var(--teal); }
  .date-day { top: 420px; font-family: "Arimo", sans-serif; font-weight: 700; font-size: 40px; color: var(--red); letter-spacing: -0.5px; }
  .date-number { top: 462px; font-family: "Arimo", sans-serif; font-weight: 700; font-size: 94px; line-height: 1; color: var(--navy); letter-spacing: 3px; padding-left: 3px; }
  .date-time { top: 566px; font-family: "Arimo", sans-serif; font-weight: 700; font-size: 44px; color: var(--teal); }
  .address-ribbon { position: absolute; left: 70px; top: 659px; width: 512px; height: 56px; }
  .address-ribbon svg { position: absolute; inset: 0; }
  .address-text {
    position: absolute; inset: 0; display: flex; align-items: center; justify-content: center;
    font-family: "Arimo", sans-serif; font-size: 36px; color: var(--white);
  }
</style>
</head>
<body>
  <main class="poster">
    <div class="balloon-backdrop" role="img" aria-label="Colourful party balloons filling the background"></div>

    <header class="logo-block">
      <span class="logo-dot"></span>
      <span class="logo-name">Willowmere<br>Chiropractic</span>
    </header>

    <section class="invite-card">
      <div class="invite-frame"></div>
      <h1>
        <span class="line headline headline-years">20th</span>
        <span class="line headline headline-birthday">BIRTHDAY</span>
        <span class="line headline headline-celebration">CELEBRATION</span>
      </h1>
      <p class="line date-day">SATURDAY, NOVEMBER</p>
      <p class="line date-number">24th,2018</p>
      <p class="line date-time">12-3pm AT WCC</p>
      <div class="address-ribbon">
        <svg width="512" height="56" viewBox="0 0 512 56" aria-hidden="true">
          <polygon points="0,0 512,0 498,28 512,56 0,56 14,28" fill="var(--red)"/>
        </svg>
        <p class="address-text">2 Harbour St Eastbrook</p>
      </div>
    </section>
  </main>
</body>
</html>
```